Clear sticker design for packaging

I need 4” diameter clear stickers designed for birthdays, thank you , teachers day and all the other special days to complete my gift packaging. They will go on the top of each tube to differentiate each gift for each occasion. Our design is on craft paper and I’ve uploaded a few examples of what we are trying to achieve. Last picture is the top of our tube where the stickers will be placed. We don’t want too much color unless for Christmas and Valentine’s Day maybe! We are working with black and gold or a mixture of both mostly

```html
<!DOCTYPE html>
<html lang="en">
<head>
<meta charset="utf-8">
<title>Thank You Sticker</title>
<link rel="stylesheet" href="https://fonts.googleapis.com/css2?family=Allura&display=swap">
<style>
  :root {
    --page: #ffffff;
    --sticker-black: #050505;
    --panel-dark: #141415;
    --panel-swirl: #232325;
    --gold-light: #f3d232;
    --gold-mid: #c9971c;
    --gold-deep: #8a5e12;
    --preview-text: #e9e4d8;
  }
  html, body {
    margin: 0;
    padding: 0;
    width: 1200px;
    height: 1200px;
    overflow: hidden;
    background: var(--page);
  }
  .canvas {
    display: block;
    width: 1200px;
    height: 1200px;
  }
  .sticker-text {
    font-family: "Allura", cursive;
  }
  .sticker-text--main {
    font-size: 132px;
  }
  .sticker-text--preview {
    font-size: 26px;
    fill: var(--preview-text);
  }
</style>
</head>
<body>
<svg class="canvas" viewBox="0 0 1200 1200" xmlns="http://www.w3.org/2000/svg">
  <defs>
    <linearGradient id="gold-foil" x1="0" y1="0" x2="1" y2="1">
      <stop offset="0" stop-color="var(--gold-light)"/>
      <stop offset="0.5" stop-color="var(--gold-mid)"/>
      <stop offset="1" stop-color="var(--gold-deep)"/>
    </linearGradient>
    <radialGradient id="swirl-field" cx="0.5" cy="0.5" r="0.5">
      <stop offset="0" stop-color="var(--panel-dark)"/>
      <stop offset="1" stop-color="var(--panel-swirl)"/>
    </radialGradient>
  </defs>

  <!-- Main sticker -->
  <g class="sticker sticker--main">
    <circle class="sticker__base" cx="589" cy="550" r="330" fill="var(--sticker-black)"/>
    <circle class="sticker__swirl-pattern" cx="589" cy="550" r="308" fill="url(#swirl-field)"
            role="img" aria-label="Soft dark grey swirl pattern across the sticker face"/>
    <circle class="sticker__outer-ring" cx="589" cy="550" r="308" fill="none" stroke="url(#gold-foil)" stroke-width="5"/>
    <circle class="sticker__inner-ring" cx="589" cy="550" r="227" fill="none" stroke="url(#gold-foil)" stroke-width="3"/>

    <rect class="sticker__ornament sticker__ornament--top" x="547" y="308" width="84" height="44" rx="20"
          fill="url(#gold-foil)" role="img" aria-label="Gold knotted flourish ornament"/>
    <rect class="sticker__ornament sticker__ornament--bottom" x="547" y="740" width="84" height="44" rx="20"
          fill="url(#gold-foil)" role="img" aria-label="Gold knotted flourish ornament"/>

    <text class="sticker-text sticker-text--main" x="589" y="575" text-anchor="middle" fill="url(#gold-foil)">Thank you</text>
  </g>

  <!-- Small-size preview -->
  <g class="sticker sticker--preview">
    <circle class="sticker__base" cx="888" cy="936" r="68" fill="var(--sticker-black)"/>
    <circle class="sticker__swirl-pattern" cx="888" cy="936" r="63" fill="url(#swirl-field)"
            role="img" aria-label="Soft dark grey swirl pattern across the sticker face"/>
    <circle class="sticker__outer-ring" cx="888" cy="936" r="63" fill="none" stroke="url(#gold-foil)" stroke-width="1.5"/>
    <circle class="sticker__inner-ring" cx="888" cy="936" r="47" fill="none" stroke="url(#gold-foil)" stroke-width="1"/>
    <rect class="sticker__ornament" x="879" y="885" width="18" height="9" rx="4"
          fill="url(#gold-foil)" role="img" aria-label="Gold knotted flourish ornament"/>
    <rect class="sticker__ornament" x="879" y="978" width="18" height="9" rx="4"
          fill="url(#gold-foil)" role="img" aria-label="Gold knotted flourish ornament"/>
    <text class="sticker-text sticker-text--preview" x="888" y="942" text-anchor="middle">Thank you</text>
  </g>
</svg>
</body>
</html>
```